Simple landing page/Web presence for boutique Fund Manager, Verran Capital

We need a website presence for our funds management business. All we need is a simple landing page with some "text" about us and a link /button to our Fund Due diligence portal. the "text" we would like to see is: "Verran Capital Pty Ltd. Its Trustee is Bellmont Trust Partners Ltd - also based in Sydney. Bellmont is the holder of an Australian Financial Services License (no.731205) whilst Verran Capital operates under a Corporate Authorised Representation from Bellmont."

We have the attached logo

```html
<!DOCTYPE html>
<html lang="en">
<head>
<meta charset="utf-8">
<title>Verran Capital</title>
<link href="https://fonts.googleapis.com/css2?family=Questrial&family=Nunito+Sans:wght@700;800&family=Montserrat:wght@500;700&display=swap" rel="stylesheet">
<style>
  :root {
    --ink: #000000;
    --paper: #ffffff;
    --page-grey: #ebebeb;
    --footer-ink: #222222;
    --hero-top: #283e55;
    --hero-mid: #6b5a5c;
    --hero-glow: #b07a5a;
    --hero-water: #3d4650;
    --photo-light: #d9cfc6;
    --photo-pink: #d6a9a6;
    --photo-wood: #a27a5c;
  }
  * { margin: 0; padding: 0; box-sizing: border-box; }
  html, body { width: 1200px; height: 1022px; overflow: hidden; }
  body {
    position: relative;
    background: var(--page-grey);
    font-family: "Questrial", sans-serif;
    color: var(--ink);
  }
  .hero {
    position: absolute; left: 0; top: 0; width: 1200px; height: 696px;
    background:
      linear-gradient(180deg, rgba(0,0,0,0.15) 0%, rgba(0,0,0,0) 40%, rgba(0,0,0,0.25) 100%),
      linear-gradient(180deg, var(--hero-top) 0%, var(--hero-mid) 30%, var(--hero-glow) 42%, var(--hero-mid) 55%, var(--hero-water) 75%, #2c3440 100%);
  }
  .brand-mark {
    position: absolute; left: 130px; top: 32px; width: 50px; height: 50px;
    background: var(--paper);
  }
  .brand-rule {
    position: absolute; left: 204px; top: 0; width: 1px; height: 111px;
    background: var(--paper); opacity: 0.8;
  }
  .brand-name {
    position: absolute; left: 221px; top: 40px;
    font-family: "Montserrat", sans-serif; font-weight: 500;
    font-size: 13.5px; line-height: 13.5px; letter-spacing: 2.6px;
    color: var(--paper); text-transform: uppercase;
  }
  .nav { position: absolute; top: 31px; left: 815px; display: flex; gap: 7px; }
  .nav a {
    display: flex; align-items: center; justify-content: center;
    height: 41px; font-family: "Nunito Sans", sans-serif; font-weight: 800;
    font-size: 15px; letter-spacing: 0.8px; text-decoration: none; text-transform: uppercase;
  }
  .nav .about { width: 107px; background: var(--paper); color: var(--ink); }
  .nav .diligence { width: 142px; background: var(--ink); color: var(--paper); }
  .menu { position: absolute; left: 1154px; top: 42px; }
  .side-rule {
    position: absolute; left: 1132px; top: 0; width: 1px; height: 720px;
    background: var(--paper); opacity: 0.6;
  }
  .pager { position: absolute; left: 1165px; top: 308px; }
  .socials { position: absolute; left: 1160px; top: 494px; display: flex; flex-direction: column; gap: 19px; }
  .socials span { display: block; width: 16px; height: 16px; border-radius: 50%; background: var(--paper); }
  .welcome {
    position: absolute; left: 0; width: 1200px; top: 262px; text-align: center;
    font-family: "Montserrat", sans-serif; font-weight: 700; font-size: 24px;
    letter-spacing: 13px; color: var(--paper); text-transform: uppercase;
  }
  .title {
    position: absolute; left: 0; width: 1200px; top: 303px; text-align: center;
    font-family: "Nunito Sans", sans-serif; font-weight: 800; font-size: 52px;
    color: var(--paper); text-transform: uppercase; letter-spacing: 0.5px;
  }
  .about-card {
    position: absolute; left: 126px; top: 486px; width: 948px; height: 454px;
    background: var(--paper); box-shadow: 0 4px 14px rgba(0,0,0,0.25);
  }
  .about-photo {
    position: absolute; left: 38px; top: 44px; width: 582px; height: 370px;
    background: radial-gradient(ellipse at 45% 50%, var(--photo-pink) 0%, #c99a8e 35%, var(--photo-light) 70%, var(--photo-wood) 100%);
  }
  .about-text {
    position: absolute; left: 488px; top: 62px; width: 417px; height: 333px;
    background: var(--ink); color: var(--paper);
    padding: 36px 30px 0 56px; font-size: 17.5px; line-height: 31px;
  }
  .about-text p + p { margin-top: 31px; }
  .footer {
    position: absolute; left: 0; width: 1200px; top: 969px; text-align: center;
    font-size: 16px; color: var(--footer-ink);
  }
  .footer a { color: inherit; text-decoration: none; }
</style>
</head>
<body>
  <header class="hero" role="img" aria-label="Dusk view of Sydney harbour with the opera house and city skyline">
  </header>

  <div class="brand-mark"></div>
  <div class="brand-rule"></div>
  <div class="brand-name">Verran<br>Capital</div>

  <nav class="nav">
    <a class="about" href="#about">About Us</a>
    <a class="diligence" href="#due-diligence">Due Diligence</a>
  </nav>

  <svg class="menu" width="27" height="21" viewBox="0 0 27 21" aria-label="Menu">
    <rect x="0" y="0" width="27" height="4" fill="#fff"/>
    <rect x="0" y="8.5" width="27" height="4" fill="#fff"/>
    <rect x="0" y="17" width="27" height="4" fill="#fff"/>
  </svg>

  <div class="side-rule"></div>

  <svg class="pager" width="14" height="82" viewBox="0 0 14 82" aria-label="Section navigation">
    <circle cx="7" cy="6" r="6" fill="#fff"/>
    <circle cx="7" cy="29" r="6" fill="#fff"/>
    <circle cx="7" cy="51" r="6" fill="#fff"/>
    <circle cx="7" cy="74" r="5" fill="none" stroke="#fff" stroke-width="2.2"/>
  </svg>

  <div class="socials" aria-label="Social links">
    <span></span><span></span><span></span><span></span><span></span>
  </div>

  <p class="welcome">Welcome to</p>
  <h1 class="title">Verran Capital</h1>

  <section class="about-card" id="about">
    <div class="about-photo" role="img" aria-label="Hands cupping a pink ceramic piggy bank"></div>
    <div class="about-text">
      <p>Verran Capital Pty Ltd. Its Trustee is Bellmont Trust Partners Ltd - also based in Sydney.</p>
      <p>Bellmont is the holder of an Australian Financial Services License (no.731205) whilst Verran Capital operates under a Corporate Authorised representative from Bellmont.</p>
    </div>
  </section>

  <footer class="footer">Copyright © 2020 Verran Capital. All Rights Reserved. <a href="#sitemap">Sitemap</a></footer>
</body>
</html>
```